Website Design for Solar Panel Company

We are working with a company called VoltaryNX.

Some sites to use for content/competitors and inspiration:
https://www.brightmoor.example
https://prod.cld-prod.raylumen.example
https://amberfieldvolt.example
https://www.korvane.example/solarpanels

Thank you for taking the time to consider designing a website for us. We are web developers based in Stockton, CA, USA. Most of our projects go through the same process. Understanding this process may help you win a project with us. We custom-code all of our websites in-house. We don’t have any requirements as to what tools you use for your design, but we prefer Figma files. For any design that we label as four-stars, we send it to the client for review. The client picks the final design they want us to use. Once we complete this process, we will continue to show additional clients all the four-star sites and purchase them later. Your designs will have multiple chances to sell. For better chances of success, we ask that you follow these guidelines.

IMAGES:
If you use any images or icons in the design, we ask that you have a link to the asset so we can purchase the image/icon. Most of the designs we submit do not have the customer’s images on them unless they have some great images. Be creative; show us the feeling you are trying to portray with your image choices. Use any royalty-free site you choose. We subscribe to Quillex and mainly use their images, but we can purchase images outside of Quillex. PLEASE NOTE: we will not submit designs to clients with watermarks on the images.

FONTS:
We ask that you identify the fonts used in the design. This can be done in a message if you want. We typically use Marlowe Fonts and Quillex Fonts.

CONTENT:
We're always open to different content and ideas. We often submit designs with stock images so the client can see our vision. We typically take pictures after the website launch to use their images with our vision. Lorem Ipsum is fine for paragraphs, but we ask that you write the headers in correct English. We want to be able to show the vision and identify the sections of the website.

INSPIRATION:
We typically add a couple of links in the brief of websites we like to help you get started in your design.

REVISIONS:
We do not often ask for revisions of the designs unless we see something in the design that may not appeal to the client. If there are slight changes that we want to make, we do that in the development process.

FEEDBACK:
We rarely give feedback on designs during the design process. We are working on many website projects and do not have the time to provide feedback. We usually respond if your request is well thought out and asks specific questions, but a note asking “feedback, please” usually goes unanswered.

```html
<!DOCTYPE html>
<html lang="en">
<head>
<meta charset="utf-8">
<title>VoltaryNX — Solar Energy</title>
<link href="https://fonts.googleapis.com/css2?family=Jost:wght@300;400;500;600;700&family=Poppins:wght@400;500;600;700&display=swap" rel="stylesheet">
<style>
:root{
  --green:#3aa31a;
  --green-light:#6fdc2c;
  --green-dark:#2a8a10;
  --ink:#111111;
  --text:#333333;
  --muted:#666666;
  --grey:#f5f5f5;
  --field:#f1f1f1;
  --footer:#121212;
  --white:#ffffff;
}
*{margin:0;padding:0;box-sizing:border-box}
html,body{width:1200px;height:4574px;overflow:hidden}
body{position:relative;background:var(--white);font-family:"Jost",sans-serif;color:var(--text)}
.abs{position:absolute}
.btn{position:absolute;display:flex;align-items:center;justify-content:center;color:var(--white);font-family:"Poppins",sans-serif;font-weight:600;font-size:14px;letter-spacing:.3px;background:linear-gradient(90deg,var(--green),var(--green-light));text-decoration:none}
.eyebrow{position:absolute;color:var(--green);font-size:16px;font-weight:400;text-transform:uppercase}
.heading{position:absolute;font-family:"Poppins",sans-serif;font-weight:600;color:var(--ink);text-transform:uppercase}

/* nav */
.site-nav{position:absolute;left:0;top:0;width:1200px;height:84px;background:var(--white);box-shadow:0 1px 4px rgba(0,0,0,.08);z-index:5}
.brand{position:absolute;left:43px;top:22px;font-family:"Poppins",sans-serif;font-weight:700;font-size:30px;color:var(--ink);letter-spacing:.5px}
.nav-links{position:absolute;top:32px;left:288px;font-size:17px;color:var(--ink);text-transform:uppercase}
.nav-links span{position:absolute;white-space:nowrap}
.nav-phone{position:absolute;left:1012px;top:27px;width:150px;height:34px;font-size:15px;font-family:"Jost",sans-serif;font-weight:500}

/* hero */
.hero{position:absolute;left:0;top:84px;width:1200px;height:700px;background:linear-gradient(180deg,#4f5e68 0%,#2d3a2c 45%,#243a1e 75%,#3c5a22 100%)}
.hero-title{position:absolute;left:36px;top:122px;width:560px;font-family:"Poppins",sans-serif;font-weight:700;font-size:56px;line-height:68px;color:var(--white);text-transform:uppercase}
.hero-text{position:absolute;left:46px;top:288px;width:520px;font-size:15px;line-height:19px;color:var(--white)}
.call-circle{position:absolute;left:797px;top:450px;width:304px;height:304px;border-radius:50%;background:var(--white);border:24px solid var(--green);text-align:center;padding-top:88px}
.call-circle .label{font-family:"Poppins",sans-serif;font-size:26px;font-weight:500;color:var(--ink)}
.call-circle .num{font-family:"Poppins",sans-serif;font-size:27px;font-weight:600;color:var(--green);margin-top:6px}

/* why */
.features{position:absolute;top:985px;left:0;width:1200px}
.feature{position:absolute;width:300px;text-align:center;font-size:25px;line-height:32px;color:var(--ink)}
.feature svg{display:block;margin:0 auto 14px}

/* about */
.about-photo{position:absolute;left:64px;top:1475px;width:436px;height:302px;border-radius:14px;background:linear-gradient(160deg,#cfe2ee 0%,#6f8a5c 45%,#6d7f96 75%,#a8bccc 100%)}
.about-text{position:absolute;left:570px;top:1580px;width:520px;font-size:14px;line-height:18px;color:var(--muted)}
.checks{position:absolute;left:572px;top:1632px}
.checks li{list-style:none;display:flex;align-items:center;gap:8px;height:46px;font-size:16px;color:var(--ink);font-family:"Poppins",sans-serif}

/* contact */
.contact-item{position:absolute;left:90px;display:flex;gap:14px;align-items:center}
.contact-item .ico{width:38px;height:38px;border-radius:50%;background:var(--green);display:flex;align-items:center;justify-content:center}
.contact-item .k{font-size:14px;color:var(--ink);font-weight:500;text-transform:uppercase;line-height:16px}
.contact-item .v{font-size:20px;color:var(--muted);line-height:22px}
.field{position:absolute;background:var(--field);border-radius:6px;font-family:"Poppins",sans-serif;font-size:13px;color:#666;padding:16px 16px 0}

/* save */
.save-text{position:absolute;left:74px;width:465px;font-size:12.5px;line-height:16px;color:var(--muted)}
.video{position:absolute;left:659px;top:2805px;width:436px;height:300px;border-radius:14px;background:linear-gradient(170deg,#8a9aa6 0%,#5c6b72 50%,#3e5a2e 85%,#4f7a2a 100%)}
.play{position:absolute;left:190px;top:121px;width:58px;height:58px;border-radius:50%;background:rgba(111,220,44,.45);display:flex;align-items:center;justify-content:center}
.play span{width:38px;height:38px;border-radius:50%;background:var(--green-light);display:flex;align-items:center;justify-content:center}

/* blog */
.post{position:absolute;top:3582px;width:204px}
.post .thumb{height:240px;border-radius:12px}
.post p{margin-top:24px;font-size:13.5px;line-height:25px;color:var(--ink);text-decoration:underline;padding-left:10px}

/* footer */
.footer-col{position:absolute;top:4234px;color:var(--white)}
.footer-col h4{font-size:22px;font-weight:400;text-transform:uppercase;margin-bottom:16px}
.footer-col li{list-style:none;display:flex;align-items:center;gap:10px;font-size:15.5px;height:44px}
.f-brand{position:absolute;left:71px;top:4224px;font-family:"Poppins",sans-serif;font-weight:700;font-size:38px;color:var(--white)}
.f-about{position:absolute;left:71px;top:4300px;width:320px;font-size:11.5px;line-height:15px;color:#ddd}
.social{position:absolute;top:4375px;width:18px;height:18px;border-radius:50%;border:2px solid var(--white)}
.newsletter-input{position:absolute;left:960px;top:4266px;width:177px;height:34px;background:var(--white);color:#888;font-size:12px;display:flex;align-items:center;justify-content:center}
.copyright{position:absolute;top:4530px;font-size:12px;color:#ddd}
</style>
</head>
<body>

<header class="site-nav">
  <div class="brand">VoltaryNX</div>
  <nav class="nav-links">
    <span style="left:0">Home</span>
    <span style="left:106px">About Us</span>
    <span style="left:242px">Services</span>
    <span style="left:384px">Prices</span>
    <span style="left:491px">FAQs</span>
    <span style="left:589px">Contact</span>
  </nav>
  <a class="btn nav-phone">
    <svg width="14" height="14" viewBox="0 0 24 24" style="margin-right:5px"><path fill="#fff" d="M6.6 10.8c1.4 2.8 3.8 5.1 6.6 6.6l2.2-2.2c.3-.3.7-.4 1-.2 1.1.4 2.3.6 3.6.6.6 0 1 .4 1 1V20c0 .6-.4 1-1 1C10.6 21 3 13.4 3 4c0-.6.4-1 1-1h3.5c.6 0 1 .4 1 1 0 1.2.2 2.4.6 3.6.1.3 0 .7-.2 1z"/></svg>+123 456 7890
  </a>
</header>

<section class="hero">
  <div role="img" aria-label="Rows of solar panels on a grassy field under a sunny sky" class="abs" style="inset:0;background:radial-gradient(circle at 73% 22%,rgba(255,240,190,.55),transparent 22%)"></div>
  <h1 class="hero-title">VoltaryNX</h1>
  <p class="hero-text">Lorem ipsum dolor sit amet, consectetur adipiscing elit, sed do eiusmod tempor incididunt ut labore et dolore magna aliqua.</p>
  <a class="btn" style="left:41px;top:362px;width:149px;height:32px">GET A QUOTE</a>
  <svg class="abs" style="left:0;top:500px" width="1200" height="202" viewBox="0 0 1200 202">
    <path d="M0 145 C120 230 330 230 520 190 C720 150 900 90 1200 115 L1200 202 L0 202 Z" fill="#fff"/>
    <path d="M0 145 C120 230 330 230 520 190 C720 150 900 90 1200 115" fill="none" stroke="#3aa31a" stroke-width="14"/>
  </svg>
</section>
<div class="call-circle">
  <div class="label">CALL US</div>
  <div class="num">+123 456 7890</div>
</div>

<p class="eyebrow" style="left:0;width:1218px;text-align:center;top:865px;font-size:15px">High Quality Products</p>
<h2 class="heading" style="left:0;width:1218px;text-align:center;top:886px;font-size:35px">Why Choose Us</h2>

<div class="features">
  <div class="feature" style="left:102px;top:15px">
    <svg width="90" height="90" viewBox="0 0 90 90" fill="none" stroke="#3aa31a" stroke-width="3"><path d="M40 6h20v22h14L50 62 26 38"/><circle cx="30" cy="45" r="20"/><text x="30" y="54" text-anchor="middle" font-size="26" fill="#3aa31a" stroke="none" font-family="Jost">$</text></svg>
    Guaranteed Lowest<br>Price
  </div>
  <div class="feature" style="left:453px;top:0">
    <svg width="100" height="100" viewBox="0 0 100 100" fill="none" stroke="#3aa31a" stroke-width="3"><circle cx="50" cy="14" r="6"/><path d="M50 2v3M62 14h3M35 14h3M58 6l2-2M42 6l-2-2"/><path d="M26 28h48l8 26H18z"/><path d="M22 41h56M42 28l-3 26M58 28l3 26M50 54v26M30 80h40"/><path d="M40 80c0-8-6-12-12-12 0 8 6 12 12 12zM60 80c0-8 6-12 12-12 0 8-6 12-12 12z"/></svg>
    Integrated<br>Product Ecosystem
  </div>
  <div class="feature" style="left:798px;top:0">
    <svg width="100" height="100" viewBox="0 0 100 100" fill="none" stroke="#3aa31a" stroke-width="3"><rect x="20" y="8" width="38" height="84" rx="6"/><path d="M34 16h10"/><circle cx="52" cy="48" r="14"/><path d="M62 58l16 16"/><path d="M45 46a8 8 0 0 1 8-6"/></svg>
    System Performance<br>Monitoring
  </div>
</div>

<!-- about band -->
<svg class="abs" style="left:0;top:1215px" width="1200" height="730" viewBox="0 0 1200 730">
  <path d="M0 55 C220 150 420 110 700 90 C960 70 1070 0 1200 5 L1200 690 C1000 640 850 720 600 700 C360 680 140 640 0 715 Z" fill="#f5f5f5"/>
</svg>
<div class="about-photo" role="img" aria-label="Solar panels under tall green trees"></div>
<p class="eyebrow" style="left:572px;top:1491px;font-size:15px">Welcome To</p>
<h2 class="heading" style="left:568px;top:1510px;font-size:37px">VoltaryNX</h2>
<p class="about-text">Excepteur sint occaecat cupidatat non proident, sunt in culpa qui officia deserunt mollit anim id est laborum.</p>
<ul class="checks">
  <li><svg width="20" height="20" viewBox="0 0 20 20"><circle cx="10" cy="10" r="8" fill="none" stroke="#3aa31a" stroke-width="2.2"/><path d="M6 10l3 3 5-6" fill="none" stroke="#3aa31a" stroke-width="2.2"/></svg>Improve your family lifestyle</li>
  <li><svg width="20" height="20" viewBox="0 0 20 20"><circle cx="10" cy="10" r="8" fill="none" stroke="#3aa31a" stroke-width="2.2"/><path d="M6 10l3 3 5-6" fill="none" stroke="#3aa31a" stroke-width="2.2"/></svg>Lower your current power bills</li>
  <li><svg width="20" height="20" viewBox="0 0 20 20"><circle cx="10" cy="10" r="8" fill="none" stroke="#3aa31a" stroke-width="2.2"/><path d="M6 10l3 3 5-6" fill="none" stroke="#3aa31a" stroke-width="2.2"/></svg>Upgrade your usable space</li>
</ul>
<a class="btn" style="left:570px;top:1777px;width:149px;height:34px">GET A QUOTE</a>

<!-- contact -->
<p class="eyebrow" style="left:90px;top:2134px">Get In Touch</p>
<h2 class="heading" style="left:88px;top:2155px;font-size:37px">Contact Us</h2>
<div class="contact-item" style="top:2228px"><div class="ico"><svg width="18" height="18" viewBox="0 0 24 24"><path fill="#fff" d="M6.6 10.8c1.4 2.8 3.8 5.1 6.6 6.6l2.2-2.2c.3-.3.7-.4 1-.2 1.1.4 2.3.6 3.6.6.6 0 1 .4 1 1V20c0 .6-.4 1-1 1C10.6 21 3 13.4 3 4c0-.6.4-1 1-1h3.5c.6 0 1 .4 1 1 0 1.2.2 2.4.6 3.6.1.3 0 .7-.2 1z"/></svg></div><div><div class="k">Call Us</div><div class="v">888 888 8888</div></div></div>
<div class="contact-item" style="top:2308px"><div class="ico"><svg width="18" height="18" viewBox="0 0 24 24"><rect x="3" y="6" width="18" height="13" rx="2" fill="#fff"/><path d="M3 7l9 6 9-6" fill="none" stroke="#3aa31a" stroke-width="2"/></svg></div><div><div class="k">Send an Email</div><div class="v">info@website.com</div></div></div>
<div class="contact-item" style="top:2386px"><div class="ico"><svg width="18" height="18" viewBox="0 0 24 24"><path fill="#fff" d="M12 2a7 7 0 0 0-7 7c0 5 7 13 7 13s7-8 7-13a7 7 0 0 0-7-7zm0 9.5A2.5 2.5 0 1 1 12 6.5a2.5 2.5 0 0 1 0 5z"/></svg></div><div><div class="k">Location</div><div class="v">Your Address Here</div></div></div>

<form>
  <div class="field" style="left:461px;top:2171px;width:297px;height:36px;padding-top:10px">Your Name</div>
  <div class="field" style="left:789px;top:2171px;width:296px;height:36px;padding-top:10px">Your Phone</div>
  <div class="field" style="left:461px;top:2231px;width:297px;height:36px;padding-top:10px">Email Address</div>
  <div class="field" style="left:789px;top:2231px;width:296px;height:36px;padding-top:10px">Select Service</div>
  <div class="field" style="left:461px;top:2290px;width:624px;height:78px;padding-top:14px">Additional Message</div>
  <a class="btn" style="left:459px;top:2391px;width:623px;height:48px;font-size:13px;background:linear-gradient(90deg,#2a8a10,#6fe62c)">GET A FREE QUOTE NOW</a>
</form>

<!-- save money band -->
<svg class="abs" style="left:0;top:2565px" width="1200" height="730" viewBox="0 0 1200 730">
  <path d="M0 70 C240 150 460 100 760 60 C950 35 1090 0 1200 8 L1200 640 C1010 590 860 650 600 670 C360 690 150 630 0 710 Z" fill="#f5f5f5"/>
</svg>
<p class="eyebrow" style="left:70px;top:2842px;font-size:15px">Save Your Money</p>
<h2 class="heading" style="left:70px;top:2860px;font-size:37px">Electricity For Less</h2>
<p class="save-text" style="top:2922px">Lorem ipsum dolor sit amet, consectetur adipiscing elit, sed do eiusmod tempor incididunt ut labore et doloremagna aliqua. Ut enim ad minim veniam, quis nostrud exercitation ullamco laboris nisi ut aliquip ex ea commodo consequat.</p>
<p class="save-text" style="top:2979px">Lorem ipsum dolor sit amet, consectetur adipiscing elit, sed do eiusmod tempor incididunt ut labore et doloremagna aliqua. Ut enim ad minim veniam, quis nostrud exercitation ullamco laboris nisi ut aliquip ex ea commodo consequat.</p>
<a class="btn" style="left:75px;top:3062px;width:149px;height:34px">GET A QUOTE</a>
<div class="video" role="img" aria-label="Robot carrying a solar panel across a meadow">
  <div class="play"><span><svg width="14" height="14" viewBox="0 0 14 14"><path d="M3 1l10 6-10 6z" fill="#fff"/></svg></span></div>
</div>

<!-- blog -->
<p class="eyebrow" style="left:0;width:1158px;text-align:center;top:3458px;font-size:15px">Latest News &amp; Updates</p>
<h2 class="heading" style="left:0;width:1158px;text-align:center;top:3484px;font-size:37px">Recent From Blog</h2>
<article class="post" style="left:73px"><div class="thumb" role="img" aria-label="Robot holding a solar panel on a sunny lawn" style="background:linear-gradient(180deg,#2f9fd8 0%,#7cc4e8 50%,#8fb85a 100%)"></div><p>Lorem ipsum dolor sit amet, consectetur adipiscing elit.</p></article>
<article class="post" style="left:339px"><div class="thumb" role="img" aria-label="Solar panels on a house roof" style="background:linear-gradient(170deg,#8fa0b8 0%,#3e4a6e 55%,#9aa4ae 100%)"></div><p>Lorem ipsum dolor sit amet, consectetur adipiscing elit.</p></article>
<article class="post" style="left:605px"><div class="thumb" role="img" aria-label="Technicians installing solar panels" style="background:linear-gradient(170deg,#4a5568 0%,#2a3340 45%,#c96a2a 75%,#dfe3e8 100%)"></div><p>Lorem ipsum dolor sit amet, consectetur adipiscing elit.</p></article>
<article class="post" style="left:870px"><div class="thumb" role="img" aria-label="Solar panel edge against a blue sky" style="background:linear-gradient(180deg,#6aa6e6 0%,#a9cdf2 60%,#1f4aa0 100%)"></div><p>Lorem ipsum dolor sit amet, consectetur adipiscing elit.</p></article>

<!-- footer -->
<svg class="abs" style="left:0;top:3960px" width="1200" height="614" viewBox="0 0 1200 614">
  <path d="M0 70 C150 130 330 110 560 95 C800 80 1000 50 1200 0 L1200 614 L0 614 Z" fill="#121212"/>
</svg>
<footer>
  <div class="f-brand">VoltaryNX</div>
  <p class="f-about">Lorem ipsum dolor sit amet, consectetur adipiscing elit, sed do eiusmod temporincididunt ut labore et doloremagna aliqua.</p>
  <span class="social" style="left:72px" aria-label="Social link"></span>
  <span class="social" style="left:123px" aria-label="Social link"></span>
  <span class="social" style="left:177px" aria-label="Social link"></span>

  <div class="footer-col" style="left:442px">
    <h4>Quick Links</h4>
    <ul>
      <li><svg width="18" height="18" viewBox="0 0 20 20"><circle cx="10" cy="10" r="8" fill="none" stroke="#3aa31a" stroke-width="2.2"/><path d="M6 10l3 3 5-6" fill="none" stroke="#3aa31a" stroke-width="2.2"/></svg>Home</li>
      <li><svg width="18" height="18" viewBox="0 0 20 20"><circle cx="10" cy="10" r="8" fill="none" stroke="#3aa31a" stroke-width="2.2"/><path d="M6 10l3 3 5-6" fill="none" stroke="#3aa31a" stroke-width="2.2"/></svg>About</li>
      <li><svg width="18" height="18" viewBox="0 0 20 20"><circle cx="10" cy="10" r="8" fill="none" stroke="#3aa31a" stroke-width="2.2"/><path d="M6 10l3 3 5-6" fill="none" stroke="#3aa31a" stroke-width="2.2"/></svg>Products</li>
      <li><svg width="18" height="18" viewBox="0 0 20 20"><circle cx="10" cy="10" r="8" fill="none" stroke="#3aa31a" stroke-width="2.2"/><path d="M6 10l3 3 5-6" fill="none" stroke="#3aa31a" stroke-width="2.2"/></svg>Prices</li>
    </ul>
  </div>
  <div class="footer-col" style="left:666px">
    <h4>Opening Hours</h4>
    <ul>
      <li style="height:52px"><svg width="24" height="24" viewBox="0 0 24 24" fill="none" stroke="#3aa31a" stroke-width="2"><circle cx="12" cy="12" r="10"/><path d="M12 6v6l4 2"/></svg>Mon - Fri &nbsp;7am - 5pm</li>
      <li style="height:52px"><svg width="24" height="24" viewBox="0 0 24 24" fill="none" stroke="#3aa31a" stroke-width="2"><circle cx="12" cy="12" r="10"/><path d="M12 6v6l4 2"/></svg>Saturday - Closed</li>
      <li style="height:52px"><svg width="24" height="24" viewBox="0 0 24 24" fill="none" stroke="#3aa31a" stroke-width="2"><circle cx="12" cy="12" r="10"/><path d="M12 6v6l4 2"/></svg>Sunday - Closed</li>
    </ul>
  </div>
  <div class="footer-col" style="left:958px">
    <h4>Stay Updated</h4>
  </div>
  <div class="newsletter-input">EMAIL ADDRESS</div>
  <a class="btn" style="left:960px;top:4326px;width:177px;height:34px;font-size:13px">SIGNUP NOW</a>

  <p class="copyright" style="left:68px">Copyright 2024 VoltaryNX. All Rights Reserved.</p>
  <p class="copyright" style="left:930px">Privacy Policy | Terms &amp; Conditions</p>
</footer>

</body>
</html>
```